Brisbane IT support business needs our first business card

Hello we are a Brisbane based Information Technology company providing support and services to small and medium sized businesses. We provide a range of services and solutions.

The business name is Wattlebrook Network Computing Services, or WNCS for short.

I am looking for a business card that looks professional (don't we all want that), but most importantly, it most utilize the colours in the logo attached.

Reason: Launched late, extending so people have enough time to actually submit something.

Target Market(s)

Other business owners seeking our IT services, and also home users.

Industry/Entity Type

Business

Requirements
Must have
• Please only use the blue/orange colours in logo attached

```html
<!DOCTYPE html>
<html lang="en">
<head>
<meta charset="utf-8">
<title>WNCS Business Card</title>
<link rel="stylesheet" href="https://fonts.googleapis.com/css2?family=Arimo:wght@400;700&display=swap">
<style>
  :root {
    --teal: #0b5672;
    --teal-deep: #074a63;
    --teal-light: #12667f;
    --orange: #ef7f1a;
    --white: #ffffff;
    --mist: #eceef0;
    --backdrop: #d9dde0;
    --text-font: "Arimo", Arial, sans-serif;
  }
  * { box-sizing: border-box; margin: 0; padding: 0; }
  html, body { width: 1200px; height: 914px; overflow: hidden; }
  body {
    background: var(--backdrop);
    font-family: var(--text-font);
    display: flex;
    flex-direction: column;
    align-items: center;
    justify-content: center;
    gap: 40px;
  }
  .card {
    position: relative;
    width: 700px;
    height: 400px;
    overflow: hidden;
    box-shadow: 0 6px 18px rgba(0,0,0,0.18);
  }

  /* ---------- Back side ---------- */
  .card--back {
    background: linear-gradient(135deg, var(--teal-light) 0%, var(--teal) 45%, var(--teal-deep) 100%);
  }
  .card--back .skyline-art {
    position: absolute;
    left: 40px; top: -60px;
    width: 300px; height: 330px;
    border-radius: 50%;
    background: radial-gradient(circle at 40% 60%, rgba(255,255,255,0.14), rgba(255,255,255,0.05) 70%);
  }
  .card--back .brand {
    position: absolute;
    right: 50px; bottom: 90px;
  }

  /* ---------- Company name ---------- */
  .brand {
    display: flex;
    align-items: center;
    gap: 12px;
  }
  .brand__mark {
    width: 16px; height: 16px;
    flex: none;
  }
  .brand__name {
    font-size: 22px;
    font-weight: 700;
    line-height: 1.2;
  }
  .card--back .brand__mark { background: var(--orange); }
  .card--back .brand__name { color: var(--white); }
  .card--front .brand__mark { background: var(--teal); }
  .card--front .brand__name { color: var(--orange); }

  /* ---------- Front side ---------- */
  .card--front { background: var(--white); }
  .card--front .skyline-art {
    position: absolute;
    left: 80px; top: 20px;
    width: 560px; height: 340px;
    background: linear-gradient(180deg, var(--mist) 0%, rgba(236,238,240,0.4) 100%);
  }
  .card--front .brand {
    position: absolute;
    left: 40px; top: 60px;
  }
  .person {
    position: absolute;
    right: 40px; top: 128px;
    text-align: left;
  }
  .person__name {
    font-size: 27px;
    color: var(--orange);
  }
  .person__role {
    font-size: 17px;
    color: var(--teal);
    margin-top: 2px;
  }
  .band-rule {
    position: absolute;
    left: 0; right: 0;
    height: 2px;
    background: var(--orange);
  }
  .band-rule--top { top: 196px; }
  .band-rule--bottom { top: 338px; }
  .info-band {
    position: absolute;
    left: 0; right: 0;
    top: 203px; height: 128px;
    background: linear-gradient(90deg, var(--teal) 0%, var(--teal-light) 60%, var(--teal) 100%);
    color: var(--white);
  }
  .address {
    position: absolute;
    left: 40px; top: 24px;
    display: flex;
    gap: 16px;
    font-size: 16px;
    line-height: 1.3;
  }
  .contacts {
    position: absolute;
    left: 440px; top: 24px;
    list-style: none;
    font-size: 16px;
    line-height: 1.55;
  }
  .contacts li { display: flex; align-items: center; gap: 12px; }
  .icon { width: 16px; height: 16px; flex: none; fill: var(--white); }
</style>
</head>
<body>

  <section class="card card--back" aria-label="Card back">
    <div class="skyline-art" role="img" aria-label="Faint city skyline and bridge decoration"></div>
    <div class="brand">
      <span class="brand__mark"></span>
      <div class="brand__name">Wattlebrook Network Computing Services</div>
    </div>
  </section>

  <section class="card card--front" aria-label="Card front">
    <div class="skyline-art" role="img" aria-label="Faint city skyline and bridge decoration"></div>
    <div class="brand">
      <span class="brand__mark"></span>
      <div class="brand__name">WNCS</div>
    </div>

    <div class="person">
      <div class="person__name">Employee Name</div>
      <div class="person__role">Managing Director</div>
    </div>

    <span class="band-rule band-rule--top"></span>
    <div class="info-band">
      <div class="address">
        <svg class="icon" viewBox="0 0 16 16" aria-hidden="true"><path d="M8 1 0 8h2v7h4.5v-4.5h3V15H14V8h2z"/></svg>
        <p>Your Adress Inc 2nd Lane<br>Ave Marlow, QL 00000</p>
      </div>
      <ul class="contacts">
        <li>
          <svg class="icon" viewBox="0 0 16 16" aria-hidden="true"><circle cx="8" cy="4.5" r="3.5"/><path d="M1 15c0-4 3-6 7-6s7 2 7 6z"/></svg>
          0012 3456 789
        </li>
        <li>
          <svg class="icon" viewBox="0 0 16 16" aria-hidden="true"><path d="M1 3h14v10H1z M2 4l6 5 6-5" fill="none" stroke="#fff" stroke-width="1.4"/></svg>
          info@youremail.com
        </li>
        <li>
          <svg class="icon" viewBox="0 0 16 16" aria-hidden="true"><circle cx="8" cy="8" r="6.5" fill="none" stroke="#fff" stroke-width="1.4"/><path d="M1.5 8h13M8 1.5c-3 3.5-3 9.5 0 13M8 1.5c3 3.5 3 9.5 0 13" fill="none" stroke="#fff" stroke-width="1.1"/></svg>
          www.yourwebsite.com
        </li>
      </ul>
    </div>
    <span class="band-rule band-rule--bottom"></span>
  </section>

</body>
</html>
```